Project Manager Business Card for Top Architectural Firm

Update and design a stunning Senior Project Manager Business Card

MARCO T. DRUMMOND II
Senior Project Manager

H A L C Y O N
A R C H I T E C T U R E L L C.
www.HalcyonGrandEstates.example
4127 NW 52nd Ter. Suite 2308
Miami, FL 33148
C: (305) 555-0184
mdrummond.halcyongrandestates@mailbox.example

Looking to have the logo to be UV Spot ink printed and to be prominent.

Target Market(s)

High end real estate architecture construction

Industry/Entity Type

Architect

Contact Information for Business Card

MARCO T. DRUMMOND II
Senior Project Manager

H A L C Y O N
Miami, FL 33148
C: (305) 555-0184

Font styles to use
Sans Serif

Colors

Designer to choose colors to be used in the design.

Requirements
Must have
• Prominent Logo

```html
<!DOCTYPE html>
<html lang="en">
<head>
<meta charset="utf-8">
<title>Halcyon Architecture – Business Card</title>
<link rel="stylesheet" href="https://fonts.googleapis.com/css2?family=Open+Sans:wght@300;400;600;700&display=swap">
<style>
  :root {
    --backdrop: #e6e6e4;
    --card: #ffffff;
    --ink: #1b1b1b;
    --ink-soft: #3a3a3a;
    --accent: #1b6fd0;
    --accent-deep: #2a4f9c;
  }
  * { box-sizing: border-box; margin: 0; padding: 0; }
  html, body {
    width: 1200px; height: 977px; overflow: hidden;
    background: var(--backdrop);
    font-family: "Open Sans", Arial, sans-serif;
  }
  .canvas {
    position: relative; width: 1200px; height: 977px;
  }
  .card {
    position: absolute; left: 100px; top: 203px;
    width: 1000px; height: 571px;
    background: var(--card);
    box-shadow: 0 10px 30px rgba(0,0,0,0.18);
  }
  .brand {
    position: absolute; left: 90px; top: 120px; width: 340px;
    text-align: center; color: var(--ink);
    font-weight: 400;
  }
  .brand-mark {
    display: block; margin: 0 auto 34px;
    width: 120px; height: 120px; border-radius: 50%;
    background: var(--accent);
  }
  .brand-name {
    font-size: 46px; line-height: 1; letter-spacing: 10px;
    margin-right: -10px;
  }
  .brand-sub {
    margin-top: 10px; font-size: 15px; letter-spacing: 4px;
    margin-right: -4px;
  }
  .divider {
    position: absolute; left: 468px; top: 70px;
    width: 2px; height: 300px;
    background: linear-gradient(to bottom, var(--accent-deep), rgba(42,79,156,0.6) 60%, rgba(42,79,156,0));
  }
  .details {
    position: absolute; left: 510px; top: 80px; color: var(--ink-soft);
  }
  .person-name {
    font-size: 27px; font-weight: 700; color: var(--accent);
    letter-spacing: 0.5px;
  }
  .person-title {
    font-size: 15px; font-weight: 600; color: var(--ink);
    margin-top: 2px;
  }
  .address {
    margin-top: 26px; font-size: 14px; line-height: 1.35;
  }
  .contacts {
    list-style: none; margin-top: 22px; font-size: 14px; line-height: 1.35;
  }
  .contacts li { display: flex; align-items: center; gap: 10px; }
  .contacts svg { width: 13px; height: 13px; fill: var(--accent); flex: none; }
</style>
</head>
<body>
<main class="canvas">
  <article class="card">
    <div class="brand">
      <span class="brand-mark" aria-hidden="true"></span>
      <div class="brand-name">HALCYON</div>
      <div class="brand-sub">ARCHITECTURE LLC.</div>
    </div>

    <div class="divider" aria-hidden="true"></div>

    <section class="details">
      <h1 class="person-name">MARCO T. DRUMMOND II</h1>
      <p class="person-title">Senior Project Manager</p>
      <p class="address">4127 NW 52nd Ter. Suite 2308<br>Miami, FL 33148</p>
      <ul class="contacts">
        <li>
          <svg viewBox="0 0 24 24" aria-hidden="true"><path d="M6.6 10.8a15.1 15.1 0 0 0 6.6 6.6l2.2-2.2a1 1 0 0 1 1-.25 11.4 11.4 0 0 0 3.6.57 1 1 0 0 1 1 1V20a1 1 0 0 1-1 1A17 17 0 0 1 3 4a1 1 0 0 1 1-1h3.5a1 1 0 0 1 1 1c0 1.25.2 2.45.57 3.57a1 1 0 0 1-.25 1z"/></svg>
          <span>(305) 555-0184</span>
        </li>
        <li>
          <svg viewBox="0 0 24 24" aria-hidden="true"><path d="M2 5h20v14H2z M2 5l10 8 10-8" /></svg>
          <span>mdrummond.halcyongrandestates@mailbox.example</span>
        </li>
        <li>
          <svg viewBox="0 0 24 24" aria-hidden="true"><circle cx="12" cy="12" r="10"/></svg>
          <span>www.HalcyonGrandEstates.example</span>
        </li>
      </ul>
    </section>
  </article>
</main>
</body>
</html>
```